New Artwork Needed for a Wine Label

We need a wine label with the size, text, fonts being exactly like the one attached. However, we need the image of the stain glass bird and grapes being slightly different. We love this image of the bird and grapes in stained glass but can no longer use it, so we need to alter it a bit. The new name of the wine is "Sol Brava" (erase "Vermoni"). The vintage is "2023" (Not 2018) All other text is the same.

To be clear: we wish to see the stain glass artwork showing the bird and grapes to be similar to what we currently have please.

Target Market(s)

US wine drinkers

Industry/Entity Type

wine sales

Font styles to use
Other font styles liked:
• It would be best to use the fonts that you see in attached label.

Requirements
Must have
• A new image of the bird and grapes in stained glass, similar to the one I am showing you, but different enough not to be exact.
Nice to have
• A new image of the bird and grapes in stained glass
Should not have
• A different image than a bird and grapes

```html
<!DOCTYPE html>
<html lang="it">
<head>
<meta charset="utf-8">
<title>Moscato d'Asti – Sol Brava – Wine Label</title>
<link rel="stylesheet" href="https://fonts.googleapis.com/css2?family=Noto+Serif+Display:wdth,wght@62.5..100,400&display=swap">
<style>
  :root {
    --page-bg: #f2f2f2;
    --label-white: #ffffff;
    --ink: #111111;
    --glass-blue: #3a9fd8;
    --glass-teal: #5cc3c9;
    --glass-yellow: #e9c94a;
    --glass-orange: #f07a2e;
    --glass-red: #e0463a;
    --medallion-cream: #f3ecc6;
    --medallion-teal: #7fcfc4;
    --medallion-rust: #d3673a;
  }
  html, body {
    margin: 0;
    padding: 0;
    width: 1200px;
    height: 846px;
    overflow: hidden;
    background: var(--page-bg);
  }
  .wine-label {
    position: absolute;
    left: 80px;
    top: 17px;
    width: 1040px;
    height: 812px;
    background: var(--label-white);
    box-shadow: 0 10px 28px rgba(0,0,0,0.18);
    font-family: "Noto Serif Display", "Times New Roman", serif;
    color: var(--ink);
  }
  .label-art {
    position: absolute;
    left: 0;
    top: 0;
    width: 1040px;
    height: 506px;
    display: block;
  }
  .label-text {
    position: absolute;
    left: 0;
    width: 100%;
    margin: 0;
    text-align: center;
    white-space: nowrap;
    font-weight: 400;
  }
  .wine-name {
    top: 522px;
    font-size: 72px;
    line-height: 80px;
    font-stretch: 62.5%;
  }
  .appellation {
    top: 598px;
    font-size: 23px;
    line-height: 28px;
    font-stretch: 62.5%;
    letter-spacing: 0.6px;
  }
  .vintage {
    top: 632px;
    font-size: 60px;
    line-height: 70px;
    font-stretch: 75%;
  }
  .label-footer {
    position: absolute;
    top: 702px;
    left: 0;
    width: 100%;
    height: 80px;
  }
  .footer-item {
    position: absolute;
    top: 0;
    line-height: 80px;
    white-space: nowrap;
  }
  .volume {
    left: 198px;
    font-size: 44px;
    font-stretch: 80%;
  }
  .producer {
    left: 0;
    width: 100%;
    text-align: center;
    font-size: 62px;
    font-stretch: 80%;
  }
  .abv {
    left: 717px;
    font-size: 44px;
    font-stretch: 80%;
  }
</style>
</head>
<body>
  <main class="wine-label">
    <svg class="label-art" viewBox="0 0 1040 506" xmlns="http://www.w3.org/2000/svg">
      <defs>
        <linearGradient id="glassBand" x1="0" y1="0" x2="1" y2="0">
          <stop offset="0" stop-color="var(--glass-blue)"/>
          <stop offset="0.3" stop-color="var(--glass-teal)"/>
          <stop offset="0.45" stop-color="var(--glass-yellow)"/>
          <stop offset="0.65" stop-color="var(--glass-orange)"/>
          <stop offset="1" stop-color="var(--glass-red)"/>
        </linearGradient>
        <radialGradient id="medallionFill" cx="0.5" cy="0.35" r="0.7">
          <stop offset="0" stop-color="var(--medallion-cream)"/>
          <stop offset="0.6" stop-color="var(--medallion-teal)"/>
          <stop offset="1" stop-color="var(--medallion-rust)"/>
        </radialGradient>
      </defs>
      <rect class="glass-band" x="0" y="0" width="1040" height="428" fill="url(#glassBand)" role="img" aria-label="Stained glass mosaic background shifting from blue on the left to orange and red on the right"/>
      <rect class="band-rule" x="0" y="426" width="1040" height="8" fill="var(--ink)"/>
      <circle class="medallion" cx="519" cy="271" r="224" fill="url(#medallionFill)" stroke="var(--ink)" stroke-width="7" role="img" aria-label="Stained glass medallion of a hummingbird on a leafy branch holding a cluster of grapes"/>
    </svg>

    <h1 class="label-text wine-name">MOSCATO D’ASTI</h1>
    <p class="label-text appellation">Denominazione di Origine Controllata e Garantita</p>
    <p class="label-text vintage">2023</p>

    <div class="label-footer">
      <span class="footer-item volume">375ml e</span>
      <span class="footer-item producer">Sol Brava</span>
      <span class="footer-item abv">5% vol</span>
    </div>
  </main>
</body>
</html>
```